4 Information One pagers needed for Australia's biggest Oil & Gas Conference

KVR is a global organisation with its corporate headquarters located in Perth, Western Australia and regional offices in Brisbane, Darwin, Singapore, Korea & China.
KVR delivers dedicated project support services, incorporating but not limited to; project design, procurement, construction, installation, commissioning, operations and maintenance. Our cross industry expertise, project expertise and track record of successfully delivering international projects with blue chip clients and partners has led to our fast evolving reputation as a preferred supplier worldwide within the oil and gas industry onshore and offshore within both greenfield and brownfield scopes.

Need to get information on a one page handout. There are 4 documents that need to be developed.

We need a banner across the top and bottom of each page, which has our logo, title of the document, and our contact details (Head Office – Address: Unit 17, 46-48 Marlow Lane, Perth WA 6000 Australia. Phone: +61 8 9371 5086) Needs to keep with the KVR colours but use images that are relevant to the oil and gas/commissioning industries. Our previous “who we are” flyer is attached so you have a feel for what we are after.

Page 1: KVR’ service offerings include (for each take brief paragraph from document attached for description of each. If unable to find information please contact us or search on www.brenvatek.com):
• Engineering Design;
• Construction Management;
• Commissioning (Systems, Processes, Resources);
• Completions Strategy;
• Multi-Disciplinary Engineering;
• Multi-Disciplinary Technicians;
• Operations & Maintenance Support;
• EX Inspect & Maintain;
• On Site Nitrogen Production;
• Water Treatment;
• Compact Separation Systems;
• Processes to support services;
o Technology to improve efficiency and productivity (Finishline Relay, TW Relay).

Page 2: Our Team – please complete in order listed below and images are attached
Derek Halvorsen
Chief Executive Officer (CEO)
An extensively experienced and practical executive in the engineering industry with over 20 years’ service, more specifically in the oil and gas sector, since 1988.
The experience has been gained through a wide array of projects throughout Australia and Overseas working in the area of Design, System Analysing, Commissioning and Construction before commencing in Business Development and then finally Company Management and Directorships.
Derek has gained extensive experience in line and project management roles and more particularly in change management, people development and team motivation.
He has extensive experience leading and working in teams associated with design, construction and commissioning of world scale capital projects in both ‘brownfields’ and ‘Greenfields’ scenarios.
Simon Whitlock
Chief Financial Officer
Simon is a qualified accountant (CGMA, CMA, CPA. MAAT) and brings to the team over 20 years of Australian and International experience in a number of key financial roles at both ASX listed and private companies. Simon comes to the team with a strong financial, commercial and business analytical skills combined with proven effective leadership of finance teams. Simon has significant experience in managing working capital requirements of growth businesses with an international footprint. Simon is a member of Southern Guild of Registered Ledger Keepers, Royal College of Business Bookkeepers & Federation of Ledger Practitioners.

Clara Venditti
HR Manager
Clara has more than 10 years’ experience across Oil & Gas, Resources, Engineering, and Finance industries. With general human resources experience, Clara has led strategic and operational HR support and services across recruitment, on boarding, training, remuneration and benefits, employment contract management, career planning and organisational accreditation for 457 visas. Further to this Clara has also managed HR within the M & A environment, through due diligence and post-acquisition integration on both buy and sell sides within the context of global organisations.

Gregory Lane
Project Services & Agency Representative
Project Services and Management expertise with local and international experience in the oil & gas, mining, and utilities industries, as well as a strong understanding within the finance sector. Andrew’s strengths and experience lie in developing and executing business proposals, as well as liaising with external consultants and clients. Possessing competent financial and economic modelling skills and the ability to utilise data for risk and profit based outcomes. Andrew has managed ISO 9001 implementation and ensures that all quality assurance processes are adhered to.
Andrew holds both Bachelor of Commerce and Master of Commerce (Economics & Finance) degrees and is working towards a Master of Science (Energy).

Martin Dunleavy
Director: KVR NT
Andrew has lived in the North of Australia for the last 26 years, bringing valuable local knowledge to the KVR NT office. He has owned and operated his NT services business for 17 years; servicing local and international clients before concentrating and moving into the Oil & Gas and Mining Sector. Andrew has many years of experience in logistics, service and supply, his extensive experience in the NT comes from the following industries: Oil & Gas; Mining; Exploration; Pastoral, Commercial Marine; and Construction.

Trevor Hanlon
Business Development Manager- Queensland
Trevor is a professional civil and mechanical engineer with more than 40 years’ experience in Australia and internationally, across consulting, construction and manufacturing sectors at operational and executive levels. He has held a number of senior executive roles with companies including Rendle Valve Systems, KTV Varnor, and Coastline Transit and has served on a number of industry associations, government committees and private sector boards.

Trevor has broad knowledge and experience in Australian and international business, with an extensive professional network throughout Australia, Asia, Europe and the United States. He has manufactured and supplied products to the oil and gas, petrochemical, power, water, military and nuclear industries.

Page 3: Our Influence
We need the headlines and logos of the following articles and publications:
https://www.tradewirejournal.com.au/article/KVR-buys-Singapore-recruitment-firm?sthash_Q7HkRmWp_tzbe=
http://www.fuelreportdaily.net/storyview.asp?storyID=512847391§ion=Careers+%26+Recruitment§ionsource=s318&aspdsc=yes#.KpdRwtH83MZ.linkedin
http://www.fuelreportdaily.net/storyview.asp?storyID=512847652§ion=Industry+Moves§ionsource=s91&Highlight=kvr&aspdsc=yes
Southern Crude & Fuel Review – this one is getting published soon so just the logo for this one at this time?

Page 4: Who we work with?
Need to have just all logos of the companies that we have worked with. Attached is logos of our clients to match the list below. May need to find better resolution ones.
- Voltrax
- Condor Energy
- Veranta Global
- Fernholt
- PBW – Pelican Boring Worldwide
- Moventa
- Starke Petrol
- Hanbit Fuel Development Company
- Crest
- TQ Group
- LW
- Zephra Rotors
- Orrin Petroleum
- Keta Energy
- Brackwell Alloys Group (BAG)
- Pinnacle Energy
- Tirolo Resources
- Millbrook Meats
- Dorvan
- Hartigan Ledger
- Veshar South Korea
- Kelt Ridge Iron Ore
- Worldwide Utility Holdings
- Falcon Oil
- Tandrel
- Brundle Nickel
- Vintro Oil
- Durvane
- KMT
- Thornbury Alumina

• DIN Offc

• 4 separate pages:
• 1. Menu of Services
• 2. Our Team
• 3. Our Influences (media companies)
• 4. Who we work with
• Keep in colours of KVR and ensure same header/footer used for all 4 pages
• orange = #D76927, R-215 G-105 B-39, CMYK C-11.65 M-70.4 Y-100 K-1.52
• Blue = #21224B, R-33 G-34 B-75, CMYK C-95.65, M-92.65 Y-39.82, K40.01
• Same theme across all 4
• Visually appealing
• Brief information
• Colour
• Images
• Made up information - if unsure please contact us

```html
<!DOCTYPE html>
<html lang="en">
<head>
<meta charset="utf-8">
<title>KVR’ service offerings</title>
<link rel="stylesheet" href="https://fonts.googleapis.com/css2?family=Open+Sans:wght@400;600;700;800&display=swap">
<style>
  :root {
    --orange: #D76927;
    --orange-light: #F0974A;
    --navy: #21224B;
    --peach: #FDDDBB;
    --rust: #A4552A;
    --ink: #111111;
    --white: #ffffff;
  }
  * { margin: 0; padding: 0; box-sizing: border-box; }
  html, body { width: 860px; height: 1200px; overflow: hidden; background: var(--white); }
  body { font-family: "Open Sans", Arial, sans-serif; color: var(--ink); }
  .sheet { position: relative; width: 860px; height: 1200px; overflow: hidden; }

  .top-bar {
    position: absolute; left: 0; top: 0; width: 860px; height: 58px;
    background: var(--orange);
  }
  .top-bar .phone {
    position: absolute; right: 38px; top: 12px;
    color: var(--white); font-size: 23px; font-weight: 600;
  }

  .brand {
    position: absolute; font-weight: 800; color: var(--navy);
    letter-spacing: 2px; line-height: 1;
  }
  .brand-header { left: 44px; top: 66px; font-size: 96px; }
  .brand-footer { left: 604px; top: 1046px; font-size: 84px; }

  .page-title {
    position: absolute; left: 310px; top: 88px;
    font-size: 45px; font-weight: 700; letter-spacing: -0.5px;
  }
  .head-office {
    position: absolute; left: 40px; top: 203px;
    font-size: 21px; font-weight: 600; color: var(--orange-light);
  }

  .streams {
    position: absolute; left: 43px; top: 270px; width: 240px; height: 424px;
    background: var(--peach); padding: 6px 6px 0 9px; overflow: hidden;
  }
  .streams h2 { font-size: 25px; font-weight: 700; line-height: 1.3; margin-bottom: 2px; }
  .streams ul { list-style: none; font-size: 13.6px; line-height: 21.3px; letter-spacing: -0.25px; }
  .streams li { position: relative; padding-left: 12px; }
  .streams li::before { content: "•"; position: absolute; left: 0; font-size: 11px; }
  .software-name {
    margin: 8px 0 0 38px; color: var(--white);
    font-size: 28px; line-height: 36px; font-weight: 700; letter-spacing: -0.5px;
  }

  .hero-photo {
    position: absolute; left: 311px; top: 270px; width: 549px; height: 411px;
    background: linear-gradient(180deg, #1f4f86 0%, #1b5a9a 40%, #0f3f78 100%);
  }

  .who-we-are {
    position: absolute; left: 0; top: 713px; width: 290px; height: 425px;
    background: var(--rust); color: var(--white); padding: 0 6px 0 22px; overflow: hidden;
  }
  .who-we-are h2 { font-size: 24px; font-weight: 600; text-align: center; line-height: 32px; padding-top: 0; margin-bottom: 4px; }
  .who-we-are p { font-size: 10.4px; line-height: 18.7px; letter-spacing: -0.2px; text-indent: 44px; }

  .services-title {
    position: absolute; left: 312px; top: 716px;
    font-size: 32px; font-weight: 700; color: var(--orange-light);
  }
  .services-list {
    position: absolute; top: 755px; list-style: none;
    font-size: 15.5px; line-height: 30px;
  }
  .services-list li { position: relative; padding-left: 12px; }
  .services-list li::before { content: "•"; position: absolute; left: 0; font-size: 12px; }
  .services-col-1 { left: 312px; width: 250px; }
  .services-col-2 { left: 568px; width: 222px; }

  .bottom-bar {
    position: absolute; left: 0; top: 1138px; width: 860px; height: 62px;
    background: var(--orange); color: var(--white);
  }
  .bottom-bar .address { position: absolute; left: 20px; top: 22px; font-size: 14px; font-weight: 600; }
  .bottom-bar .phone { position: absolute; right: 26px; top: 15px; font-size: 21px; font-weight: 600; }
</style>
</head>
<body>
<div class="sheet">
  <header class="top-bar">
    <div class="phone">Phone: +61 8 9371 5086</div>
  </header>

  <div class="brand brand-header">KVR</div>
  <h1 class="page-title">KVR’ service offerings</h1>
  <div class="head-office">Head Office – Address: Unit 17, 46-48 Marlow Lane, Perth WA 6000 Australia.</div>

  <section class="streams">
    <h2>Six core business streams are offered:</h2>
    <ul>
      <li>Project Engineering Management (Multi-discipline)</li>
      <li>Completions &amp; CommissioningServices (Systems, Processes,Resources)</li>
      <li>Hazardous Area Validation &amp; Inspection</li>
      <li>Specialist Identification Deployment and Management</li>
      <li>Agencies</li>
      <li>Technology- 3rd Generation Commissioning Software:</li>
    </ul>
    <div class="software-name">relay</div>
  </section>

  <div class="hero-photo" role="img" aria-label="Semi-submersible offshore drilling rig standing in deep blue open sea"></div>

  <section class="who-we-are">
    <h2>Who we are?</h2>
    <p>KVR is a specialist asset support services provider with operations in Perth, Singapore, Brisbane, Darwin and China. Our expertise lies in oil and gas, mining, utilities and infrastructure projects.</p>
    <p>Whether onshore or offshore, greenfields or brownfields, we work within your teams or independently, assembling the right resources for your requirements.</p>
    <p>Your requirements may lie on our specialist areas of completions and commissioning, operational readiness, or specialist inspections. Or they may be more general engineering requirements.</p>
    <p>KVR has broad experience across all aspects of the asset support lifecycle, from concept studies and project planning, to startup and ongoing maintenance.</p>
    <p>Whatever your project requirements, wherever you operate, whatever your timeframes – KVR is your partner for success.</p>
  </section>

  <h2 class="services-title">Services</h2>
  <ul class="services-list services-col-1">
    <li>Engineering Design;</li>
    <li>Construction Management;</li>
    <li>Commissioning (Systems, Processes, Resources);</li>
    <li>Completions Strategy;</li>
    <li>Multi-Disciplinary Engineering;</li>
    <li>Multi-Disciplinary Technicians;</li>
    <li>Operations &amp; Maintenance Support;</li>
    <li>EX Inspect &amp; Maintain;</li>
    <li>On Site Nitrogen Production;</li>
    <li>Water Treatment;</li>
  </ul>
  <ul class="services-list services-col-2">
    <li>Compact Separation Systems;</li>
    <li>Processes to support services;</li>
    <li>Technology to improve efficiency and productivity (Finishline Relay, TW Relay).</li>
  </ul>

  <div class="brand brand-footer">KVR</div>

  <footer class="bottom-bar">
    <div class="address">Head Office – Address: Unit 17, 46-48 Marlow Lane, Perth WA 6000 Australia.</div>
    <div class="phone">Phone: +61 8 9371 5086</div>
  </footer>
</div>
</body>
</html>
```